Stationery for consulting company
Strategic Thinking. Inclusive Solutions. Measurable Impact
Project: Stationery for consulting company
Business Cards and Stationery
Professional
Benedo Ofurame Phd
Senior Partner
Plot 9 Umoru Close Oregun, Ikeja Lagos - Nigeria
Benedo.ofura@velmarq.com
www.velmarq.com
fdsfdffdsd

```html
<!DOCTYPE html>
<html lang="en">
<head>
<meta charset="utf-8">
<title>Velmarq Consulting – Business Card</title>
<link rel="stylesheet" href="https://fonts.googleapis.com/css2?family=Montserrat:wght@400;500;700;800&display=swap">
<style>
  :root {
    --bg: #d9dadb;
    --orange: #d0562a;
    --orange-light: #e36a2c;
    --tan: #e4a66c;
    --green: #1d5a3b;
    --ink: #3d3d3d;
    --muted: #7a7a7a;
    --rule: #cfcfcf;
    --paper: #ffffff;
  }
  * { box-sizing: border-box; margin: 0; padding: 0; }
  html, body { width: 1200px; height: 901px; overflow: hidden; }
  body {
    background: var(--bg);
    font-family: "Montserrat", sans-serif;
    position: relative;
  }
  .card {
    position: absolute;
    left: 300px;
    width: 600px;
    border-radius: 16px;
    overflow: hidden;
  }
  .card-front {
    top: 68px;
    height: 411px;
    background: var(--orange);
    display: flex;
    align-items: center;
    justify-content: center;
    gap: 18px;
  }
  .front-mark {
    width: 40px; height: 40px;
    border-radius: 50%;
    background: var(--tan);
  }
  .front-name {
    font-weight: 800;
    font-size: 58px;
    letter-spacing: 4px;
    color: var(--tan);
  }
  .card-back {
    top: 487px;
    height: 343px;
    background: var(--paper);
  }
  .brand {
    position: absolute;
    top: 18px; right: 36px;
    display: flex; align-items: center; gap: 10px;
    color: var(--green);
  }
  .brand-dot {
    width: 38px; height: 38px; border-radius: 50%;
    background: var(--green);
  }
  .brand-text { display: flex; flex-direction: column; line-height: 1; }
  .brand-name { font-weight: 800; font-size: 28px; letter-spacing: 2px; }
  .brand-sub { font-weight: 500; font-size: 11px; letter-spacing: 6.5px; margin-top: 4px; }
  .person { position: absolute; left: 33px; top: 172px; }
  .person-name {
    font-weight: 800; font-size: 22px; color: var(--green); letter-spacing: 0.5px;
  }
  .person-name .degree { color: var(--orange); }
  .person-role { font-size: 11px; color: var(--muted); margin-top: 3px; }
  .rule {
    position: absolute; left: 33px; right: 36px; top: 230px;
    border-top: 1px solid var(--rule);
  }
  .contacts {
    position: absolute; left: 33px; top: 246px;
    list-style: none; font-size: 12px; color: var(--ink);
  }
  .contacts li { display: flex; align-items: center; gap: 8px; height: 20px; }
  .contacts svg { width: 11px; height: 11px; fill: var(--ink); }
  .address {
    position: absolute; right: 36px; top: 246px;
    text-align: right; font-size: 12px; color: var(--ink); line-height: 20px;
    font-style: normal;
  }
  .wave { position: absolute; left: 0; bottom: 0; width: 600px; height: 54px; }
  .website {
    position: absolute; right: 36px; bottom: 11px;
    font-size: 12px; font-weight: 500; color: var(--paper);
  }
</style>
</head>
<body>
  <section class="card card-front" aria-label="Card front">
    <span class="front-mark"></span>
    <span class="front-name">VELMARQ</span>
  </section>

  <section class="card card-back" aria-label="Card back">
    <div class="brand">
      <span class="brand-dot"></span>
      <div class="brand-text">
        <span class="brand-name">VELMARQ</span>
        <span class="brand-sub">CONSULTING</span>
      </div>
    </div>

    <div class="person">
      <h1 class="person-name">BENEDO OFURAME <span class="degree">PHD</span></h1>
      <p class="person-role">Senior Partner</p>
    </div>

    <div class="rule"></div>

    <ul class="contacts">
      <li>
        <svg viewBox="0 0 24 24"><path d="M6.6 10.8a15 15 0 0 0 6.6 6.6l2.2-2.2c.3-.3.7-.4 1-.2 1.1.4 2.3.6 3.6.6.6 0 1 .4 1 1V20c0 .6-.4 1-1 1A17 17 0 0 1 3 4c0-.6.4-1 1-1h3.5c.6 0 1 .4 1 1 0 1.3.2 2.5.6 3.6.1.3 0 .7-.2 1z"/></svg>
        +234 (0) 801 555 0147
      </li>
      <li>
        <svg viewBox="0 0 24 24"><path d="M2 5h20v14H2z M2 5l10 8 10-8" /></svg>
        Benedo.ofura@velmarq.com
      </li>
    </ul>

    <address class="address">
      Plot 9 Umoru Close Oregun<br>
      Ikeja Lagos - Nigeria
    </address>

    <svg class="wave" viewBox="0 0 600 54" preserveAspectRatio="none" aria-hidden="true">
      <path d="M0 6 C120 2 270 8 440 20 C300 13 150 10 0 14 Z" fill="var(--orange-light)"/>
      <path d="M0 22 C150 14 330 26 600 10 L600 54 L0 54 Z" fill="var(--green)"/>
    </svg>
    <span class="website">www.velmarq.com</span>
  </section>
</body>
</html>
```